Quillbrook Health needs a new services brochure

We need a new brochure that highlights the services that we offer at our clinic. We are a multidisciplinary health clinic that focuses on injury rehabilitation and pain management. We are looking for a brochure that will highlight our primary services to our clientele and inform potential clients of what we can offer. We pride ourselves on our quality of care and our advanced treatment techniques.
Target Market(s)
young families, athletes, people interested in their health.
Industry/Entity Type
Health And Wellness
Colors
Designer to choose colors to be used in the design.
Requirements
Must have
- We would love our new brochure to be a tri-fold that has 6 pages. We would like it to have brief information about our featured services:
- - Chiropractic
- - Massage Therapy
- - Manual Osteopathic Therapy
- - Acupuncture
- - Laser Therapy
- - Radial Shockwave Therapy
- We would also like this brochure to include a brief price list and direct billing info, About Us section & Contact information.
Nice to have
- If there is space to list that we also offer other services such as : Tissue Unwind Method, Hot Stone Massage, Cupping Technique, Pembrill Method, and Kinesiology Taping that would be great. We would like to use images similar to those that are on our website (we have hi-res of all images on the website) www.quillbrookhealth.ca and colours that would fit with our logo.

```html
<!DOCTYPE html>
<html lang="en">
<head>
<meta charset="utf-8">
<title>Quillbrook Health – Tri-fold Brochure</title>
<link rel="stylesheet" href="https://fonts.googleapis.com/css2?family=Montserrat:wght@500;700;800;900&family=Open+Sans:wght@400;600;700&display=swap">
<style>
  :root{
    --blue:#1b63c6;
    --blue-dark:#0b3f8f;
    --blue-light:#5aa3ea;
    --ink:#2b2f36;
    --muted:#5f6670;
    --paper:#ffffff;
    --stage:#e4e6e9;
    --photo-park-a:#9bb45a;
    --photo-park-b:#d8d2b8;
    --photo-room-a:#c9c2b6;
    --photo-room-b:#8a8378;
    --map:#e9ecef;
  }
  *{box-sizing:border-box;margin:0;padding:0}
  html,body{width:837px;height:1200px;overflow:hidden;background:var(--stage)}
  body{font-family:"Open Sans",Arial,sans-serif;color:var(--ink);position:relative}
  .spread{position:absolute;left:0;top:277px;width:837px;height:646px;display:flex;background:var(--paper);box-shadow:0 6px 18px rgba(0,0,0,.18)}
  .panel{position:relative;width:279px;height:646px;overflow:hidden;background:var(--paper)}
  .panel svg.deco{position:absolute;left:0;top:0}
  .heading{font-family:"Montserrat",Arial,sans-serif;font-weight:800;color:var(--blue-dark);font-size:15px;letter-spacing:.5px;text-align:center;display:flex;align-items:center;gap:8px;justify-content:center}
  .heading::before,.heading::after{content:"";height:1.5px;width:44px;background:var(--blue)}
  /* About panel */
  .about .heading{position:absolute;top:44px;left:0;right:0}
  .about .copy{position:absolute;top:74px;left:26px;right:22px;font-size:8.2px;line-height:1.55;color:var(--muted);text-align:justify}
  .billing-title{position:absolute;top:176px;left:0;right:0;text-align:center;font-family:"Montserrat",Arial,sans-serif;font-weight:800;font-style:italic;color:var(--blue-dark);font-size:15px}
  .billing-intro{position:absolute;top:198px;left:26px;right:22px;text-align:center;font-size:8px;color:var(--muted)}
  .insurers{position:absolute;top:218px;left:30px;right:20px;display:grid;grid-template-columns:1fr 1fr;column-gap:10px;row-gap:4px;list-style:none;font-size:8px;color:var(--ink)}
  .insurers li{display:flex;align-items:center;gap:5px}
  .insurers li::before{content:"";width:5px;height:5px;border-radius:50%;background:var(--blue)}
  /* Contact panel */
  .contact .heading{position:absolute;top:168px;left:0;right:0}
  .address{position:absolute;top:196px;left:0;right:0;text-align:center;font-size:8.5px;line-height:1.5;color:var(--muted)}
  .address strong{color:var(--ink);font-weight:700}
  .phone{position:absolute;top:250px;left:0;right:0;display:flex;align-items:center;justify-content:center;gap:8px;font-family:"Montserrat",Arial,sans-serif;font-weight:800;font-size:18px;color:var(--blue-dark)}
  .email{position:absolute;top:278px;left:0;right:0;text-align:center;font-size:8px;color:var(--muted)}
  .map{position:absolute;top:302px;left:28px;width:223px;height:170px;background:var(--map);border:3px solid var(--paper);box-shadow:0 0 0 1px #cfd5dc}
  .follow{position:absolute;bottom:26px;left:0;right:0;display:flex;align-items:center;justify-content:center;gap:8px;font-family:"Montserrat",Arial,sans-serif;font-weight:700;font-size:10px;color:var(--paper)}
  .social{width:14px;height:14px;border-radius:50%;background:var(--paper)}
  /* Cover panel */
  .brand{position:absolute;top:404px;left:0;right:0;display:flex;align-items:center;justify-content:center;gap:8px;font-family:"Montserrat",Arial,sans-serif;font-weight:700;font-size:20px;color:var(--blue-dark)}
  .brand-dot{width:22px;height:22px;border-radius:50%;background:var(--blue)}
  .tagline{position:absolute;top:452px;left:0;right:0;text-align:center;font-family:"Montserrat",Arial,sans-serif;font-weight:900;line-height:1;color:var(--blue-dark)}
  .tagline .l1{display:block;font-size:30px;color:var(--blue)}
  .tagline .l2{display:block;font-size:36px}
  .website{position:absolute;bottom:18px;right:22px;font-size:8.5px;font-weight:600;color:var(--paper)}
</style>
</head>
<body>
<main class="spread">

  <!-- Inside flap: about & billing -->
  <section class="panel about">
    <svg class="deco" width="279" height="646" viewBox="0 0 279 646">
      <path d="M0 0 H120 C80 10 40 24 0 44 Z" fill="var(--blue)"/>
      <path d="M0 30 C40 14 80 6 130 0 H150 C90 8 40 24 0 48 Z" fill="var(--blue-light)"/>
      <path d="M0 410 C90 440 190 430 279 395 V646 H0 Z" fill="var(--blue)"/>
      <path role="img" aria-label="Photo of the bright clinic treatment room interior" d="M0 428 C90 456 190 446 279 412 V646 H0 Z" fill="url(#room)"/>
      <defs>
        <linearGradient id="room" x1="0" y1="0" x2="0" y2="1">
          <stop offset="0" stop-color="var(--photo-room-a)"/>
          <stop offset="1" stop-color="var(--photo-room-b)"/>
        </linearGradient>
      </defs>
    </svg>
    <h2 class="heading">ABOUT US</h2>
    <p class="copy">Quillbrook Health is a multidisciplinary clinic offering chiropractic, massage therapy, acupuncture, manual osteopathy and laser therapy. Our team uses advanced treatment techniques to help you recover from injury, manage pain and get back to the activities you love. We focus on quality care for every patient.</p>
    <h3 class="billing-title">We direct bill</h3>
    <p class="billing-intro">We direct bill the following insurance providers for your convenience:</p>
    <ul class="insurers">
      <li>Harbourline Benefits</li><li>Northgate Insurance</li>
      <li>Cedarpoint Life</li><li>Trellis Group</li>
      <li>Maplecrest Health</li><li>Bluewater Mutual</li>
      <li>Ashford Plans</li><li>Kestrel Benefits</li>
      <li>Summit Assurance</li><li>Lakeview Life</li>
      <li>Ridgeway Health</li><li>Pinecrest Group</li>
    </ul>
  </section>

  <!-- Back panel: contact -->
  <section class="panel contact">
    <svg class="deco" width="279" height="646" viewBox="0 0 279 646">
      <path role="img" aria-label="Close-up photo of a therapist treating a patient's shoulder" d="M60 0 H279 V130 C210 150 120 140 60 110 Z" fill="url(#treat)"/>
      <path d="M40 0 H62 V112 C120 142 210 152 279 132 V140 C200 164 110 152 40 120 Z" fill="var(--blue)"/>
      <path d="M0 560 C80 580 190 570 279 540 V646 H0 Z" fill="var(--blue-light)"/>
      <path d="M0 574 C90 596 190 586 279 556 V646 H0 Z" fill="var(--blue)"/>
      <defs>
        <linearGradient id="treat" x1="0" y1="0" x2="1" y2="1">
          <stop offset="0" stop-color="#e2c3ad"/>
          <stop offset="1" stop-color="#b79a86"/>
        </linearGradient>
      </defs>
    </svg>
    <h2 class="heading">CONTACT US</h2>
    <p class="address"><strong>Alderwood Fitness Centre</strong><br>410 - 1275 Larchmont Way NW<br>Fernhill, AB T0X 1A0</p>
    <p class="phone">
      <svg width="16" height="16" viewBox="0 0 24 24" aria-hidden="true"><path fill="var(--blue)" d="M6.6 10.8a15.1 15.1 0 0 0 6.6 6.6l2.2-2.2a1 1 0 0 1 1-.25 11.4 11.4 0 0 0 3.6.57 1 1 0 0 1 1 1V20a1 1 0 0 1-1 1A17 17 0 0 1 3 4a1 1 0 0 1 1-1h3.5a1 1 0 0 1 1 1c0 1.25.2 2.45.57 3.57a1 1 0 0 1-.25 1z"/></svg>
      (555) 014-6220
    </p>
    <p class="email">info@quillbrookhealth.ca</p>
    <div class="map" role="img" aria-label="Street map showing the clinic location"></div>
    <p class="follow">Follow Us <span class="social"></span><span class="social"></span></p>
  </section>

  <!-- Front cover -->
  <section class="panel cover">
    <svg class="deco" width="279" height="646" viewBox="0 0 279 646">
      <path role="img" aria-label="Photo of a woman rubbing her sore neck in a sunny park" d="M0 0 H279 V330 C200 375 90 385 0 360 Z" fill="url(#park)"/>
      <path d="M0 360 C90 385 200 375 279 330 V350 C200 395 90 400 0 378 Z" fill="var(--blue)"/>
      <path d="M0 378 C90 400 200 395 279 350 V358 C200 404 90 410 0 388 Z" fill="var(--blue-light)"/>
      <path d="M0 600 C90 585 190 590 279 570 V646 H0 Z" fill="var(--blue)"/>
      <defs>
        <linearGradient id="park" x1="0" y1="0" x2="1" y2="1">
          <stop offset="0" stop-color="var(--photo-park-b)"/>
          <stop offset=".5" stop-color="var(--photo-park-a)"/>
          <stop offset="1" stop-color="#6e8a3c"/>
        </linearGradient>
      </defs>
    </svg>
    <div class="brand"><span class="brand-dot"></span>Quillbrook Health</div>
    <h1 class="tagline"><span class="l1">LIVE LIFE</span><span class="l2">PAIN FREE</span></h1>
    <p class="website">www.quillbrookhealth.ca</p>
  </section>

</main>
</body>
</html>
```